Brevanta needs a business Card Design

We are looking for a business card Design for our new Managed Service Provider Company, Brevanta. Brevanta encompasses everything IT for the average medium sized business. Our primary services are help desk support, cyber-security (malware and ransomware protection), and Disaster Recovery systems. We would like the design to have a very clean and professional look, with a very minimalist feel.

Target Market(s)

Medium to large sized businesses

Industry/Entity Type

It Service

Contact Information for Business Card

Name GoesHere
name@brevanta-mail.net
O: 555-382-6047
C: 555-000-0000

Font styles to use
Other font styles liked:
• Poppins Font Only Please

Colors

Designer to choose only greyscale colors for use in the design.

Requirements
Must have
• Logo included
Nice to have
• Cutting Edge, innovative, minimalistic, elegant

```html
<!DOCTYPE html>
<html lang="en">
<head>
<meta charset="UTF-8">
<title>Brevanta Business Card</title>
<link href="https://fonts.googleapis.com/css2?family=Poppins:wght@300;400;500&family=Oswald:wght@500&display=swap" rel="stylesheet">
<style>
  :root {
    --stage: #2a2a2a;
    --card: #1f1f1f;
    --ink: #f2f2f2;
    --ink-soft: #cfcfcf;
    --rule: #bdbdbd;
    --strip: #ffffff;
  }
  * { margin: 0; padding: 0; box-sizing: border-box; }
  html, body {
    width: 1200px; height: 901px; overflow: hidden;
    background: radial-gradient(ellipse at 70% 30%, #3a3a3a 0%, var(--stage) 60%, #1c1c1c 100%);
    font-family: "Poppins", sans-serif;
  }
  .stage {
    width: 1200px; height: 901px;
    display: flex; flex-direction: column; align-items: center; justify-content: center;
    gap: 44px;
  }
  .card {
    position: relative;
    width: 600px; height: 343px;
    background: var(--card);
    box-shadow: 0 18px 40px rgba(0,0,0,0.45);
    overflow: hidden;
  }
  /* Front */
  .card-front { display: flex; align-items: center; justify-content: center; }
  .brand {
    display: flex; align-items: center; gap: 18px;
    color: var(--ink);
    font-weight: 400; font-size: 30px; letter-spacing: 0.42em;
    text-transform: uppercase;
  }
  .brand-square { width: 14px; height: 14px; background: var(--ink); }
  /* Back */
  .contact-block {
    position: absolute; top: 110px; left: 0; right: 0;
    display: flex; justify-content: center; align-items: center; gap: 28px;
  }
  .identity { text-align: right; }
  .identity-name {
    font-family: "Oswald", sans-serif; font-weight: 500;
    font-size: 36px; line-height: 1; color: var(--ink); letter-spacing: -0.01em;
    text-transform: uppercase;
  }
  .identity-role { font-size: 17px; font-weight: 300; color: var(--ink-soft); margin-top: 4px; }
  .divider { width: 1px; height: 76px; background: var(--rule); }
  .details { list-style: none; }
  .details li {
    display: flex; align-items: center; gap: 10px;
    font-size: 17px; font-weight: 300; color: var(--ink); line-height: 1.45;
  }
  .details svg { width: 16px; height: 16px; fill: var(--ink); flex-shrink: 0; }
  .website {
    position: absolute; bottom: 44px; left: 0; right: 0; text-align: center;
    font-size: 17px; font-weight: 300; color: var(--ink-soft);
  }
  .base-strip { position: absolute; left: 0; right: 0; bottom: 0; height: 12px; background: var(--strip); }
</style>
</head>
<body>
<main class="stage">
  <section class="card card-front">
    <div class="brand"><span class="brand-square"></span>Brevanta</div>
  </section>

  <section class="card card-back">
    <div class="contact-block">
      <div class="identity">
        <div class="identity-name">Dana Mercer</div>
        <div class="identity-role">Manager</div>
      </div>
      <div class="divider"></div>
      <ul class="details">
        <li>
          <svg viewBox="0 0 24 24"><path d="M6.6 10.8a15.1 15.1 0 0 0 6.6 6.6l2.2-2.2c.3-.3.7-.4 1-.2 1.1.4 2.3.6 3.6.6.6 0 1 .4 1 1V20c0 .6-.4 1-1 1A17 17 0 0 1 3 4c0-.6.4-1 1-1h3.5c.6 0 1 .4 1 1 0 1.3.2 2.5.6 3.6.1.3 0 .7-.2 1z"/></svg>
          555-382-6047
        </li>
        <li>
          <svg viewBox="0 0 24 24"><path d="M8 1h8a2 2 0 0 1 2 2v18a2 2 0 0 1-2 2H8a2 2 0 0 1-2-2V3a2 2 0 0 1 2-2zm0 3v14h8V4zm4 15.2a1 1 0 1 0 0 2 1 1 0 0 0 0-2z"/></svg>
          555-000-0000
        </li>
        <li>
          <svg viewBox="0 0 24 24"><path d="M2 5h20v14H2zm2 2v.5l8 5.3 8-5.3V7zm0 2.9V17h16V9.9l-8 5.3z"/></svg>
          dana@brevanta-mail.net
        </li>
      </ul>
    </div>
    <div class="website">www.brevanta-mail.net</div>
    <div class="base-strip"></div>
  </section>
</main>
</body>
</html>
```